Velvet Bloom Marisol's Cleaning Service Business Cards Project

A business card with all contact details with logo design on there (already have a logo) eye catching Logo and contact info on one side, full logo on the back, must target upper class residential and corporate companies, fitness companies, still keep it on the feminine side of things , must look elegant

Target Market(s)

Upper class homes and corporate companies

Industry/Entity Type

Cleaning Service

Contact Information for Business Card

Name: Marisol Denhart
Position: Director
ABN: 47193062857
Email: marisolsvelvetcleaning@brightmail.example
Number: 0418926547

Font styles to use
Decorative

Colors

Designer to choose colors to be used in the design.

Requirements
Must have
• Available Sydney Wide, contact info and logo on one side, full logo on the back
Nice to have
• Professional appearance
Should not have
• Cheap advert looking stuff

```html
<!DOCTYPE html>
<html lang="en">
<head>
<meta charset="utf-8">
<title>Velvet Bloom – Business Cards</title>
<link rel="stylesheet" href="https://fonts.googleapis.com/css2?family=Lora:wght@400&family=Lato:wght@400&display=swap">
<style>
  :root {
    --backdrop: #8c8c8c;
    --card-light: #f4f4f4;
    --card-dark: #2b3040;
    --ink: #262a36;
    --ornament-tone: #d9dadf;
    --accent: #33d6cf;
    --emblem-tone: #353b4c;
  }
  * { margin: 0; padding: 0; box-sizing: border-box; }
  html, body { width: 1200px; height: 1200px; overflow: hidden; }
  body { background: var(--backdrop); position: relative; font-family: "Lato", sans-serif; }

  .card {
    position: absolute;
    top: 310px;
    width: 364px;
    height: 594px;
    border-radius: 14px;
    box-shadow: 2px 3px 4px rgba(0,0,0,0.35);
    overflow: hidden;
  }
  .card--front { left: 234px; background: var(--card-light); color: var(--ink); }
  .card--back { left: 627px; width: 370px; background: var(--card-dark); color: var(--accent); }

  .brand-mark {
    position: absolute;
    left: 131px;
    top: 90px;
    width: 102px;
    height: 102px;
    border-radius: 50%;
    border: 2px solid var(--ink);
  }
  .ornament {
    position: absolute;
    left: 34px;
    top: 196px;
    width: 296px;
    height: 54px;
    border-radius: 27px;
    background: linear-gradient(90deg, rgba(217,218,223,0) 0%, var(--ornament-tone) 30%, var(--ornament-tone) 70%, rgba(217,218,223,0) 100%);
  }

  .wordmark {
    position: absolute;
    left: 0; right: 0;
    text-align: center;
  }
  .wordmark__name {
    font-family: "Lora", serif;
    font-weight: 400;
    font-size: 33px;
    letter-spacing: 1px;
    line-height: 1;
  }
  .wordmark__tagline {
    font-family: "Lato", sans-serif;
    font-size: 11.5px;
    letter-spacing: 3.6px;
    margin-top: 10px;
    text-transform: uppercase;
  }
  .card--front .wordmark { top: 264px; }
  .card--back .wordmark { top: 476px; }
  .card--back .wordmark__name { font-size: 35px; }
  .card--back .wordmark__tagline { font-size: 12.5px; letter-spacing: 4px; margin-top: 11px; }

  .emblem-field {
    position: absolute;
    left: 0; top: 0;
    width: 100%; height: 594px;
    background: radial-gradient(ellipse at 50% 45%, var(--emblem-tone) 0%, var(--card-dark) 75%);
  }
  .emblem-circle {
    position: absolute;
    left: 25px;
    top: 62px;
    width: 320px;
    height: 320px;
    border-radius: 50%;
    border: 16px solid var(--emblem-tone);
  }

  .contact {
    position: absolute;
    left: 0; right: 0;
    top: 398px;
    text-align: center;
    font-size: 17px;
    line-height: 1.3;
  }
  .contact__name {
    font-family: "Lora", serif;
    font-size: 23px;
    letter-spacing: 0.5px;
    text-transform: uppercase;
  }
  .contact__role { margin-top: 2px; }
  .contact__abn { margin-top: 11px; }
  .contact__phone { margin-top: 11px; }
  .contact__email { font-size: 15.5px; }
</style>
</head>
<body>
  <section class="card card--front">
    <div class="brand-mark" aria-hidden="true"></div>
    <div class="ornament" role="img" aria-label="Decorative floral flourish beneath the brand mark"></div>
    <div class="wordmark">
      <div class="wordmark__name">VELVET BLOOM</div>
      <div class="wordmark__tagline">Marisol’s Cleaning Services</div>
    </div>
    <div class="contact">
      <div class="contact__name">Marisol Denhart</div>
      <div class="contact__role">Director</div>
      <div class="contact__abn">ABN: 47193062857</div>
      <div class="contact__phone">0418926547</div>
      <div class="contact__email">marisolsvelvetcleaning@brightmail.example</div>
    </div>
  </section>

  <section class="card card--back">
    <div class="emblem-field" role="img" aria-label="Large faint brand emblem pattern in muted slate tones"></div>
    <div class="emblem-circle" aria-hidden="true"></div>
    <div class="wordmark">
      <div class="wordmark__name">VELVET BLOOM</div>
      <div class="wordmark__tagline">Marisol’s Cleaning Services</div>
    </div>
  </section>
</body>
</html>
```